Enhance existing Powerpoint customer presentation from the visual communication viewpoint

Based on existing uploaded presentation (and embedded logos) we want a presentation that is coherent with our corporate identity, and visually appealing and convincing.

Photos and graphical elements can be changed to better transmit the ideas.

In addition, we added a single slide which should be part of that presentation. The design should be in harmony with the previous ones.

IT, Software Quality, Software Testing, Consulting

Communication

```html
<!DOCTYPE html>
<html lang="en">
<head>
<meta charset="utf-8">
<title>n-stride — Software Quality Experts</title>
<link href="https://fonts.googleapis.com/css2?family=Arimo:wght@400;700&display=swap" rel="stylesheet">
<style>
:root{
  --ink:#1d2438;
  --muted:#8a8f99;
  --frame:#c9ccd2;
  --magenta:#b5008c;
  --blue:#3f6fb4;
  --blue-dark:#2f5597;
  --blue-light:#9dc3e6;
  --alert:#d6262f;
  --paper:#ffffff;
}
*{box-sizing:border-box;margin:0;padding:0}
html,body{width:848px;height:1200px;overflow:hidden;background:var(--paper)}
body{position:relative;font-family:"Arimo",Arial,sans-serif;color:var(--ink)}
.slide{position:absolute;width:334px;height:243px;border:1px solid var(--frame);background:var(--paper);overflow:hidden}
.s1{left:86px;top:33px}.s2{left:433px;top:33px}
.s3{left:86px;top:318px}.s4{left:433px;top:318px}
.s5{left:86px;top:603px}.s6{left:433px;top:603px}
.s7{left:260px;top:888px}
.brand{position:absolute;right:12px;top:9px;font-size:9px;font-weight:700;color:var(--ink);letter-spacing:.2px}
.slide-title{position:absolute;left:18px;top:38px;width:230px;font-size:11.5px;font-weight:700;line-height:1.25}
.footer{position:absolute;left:18px;right:14px;bottom:7px;display:flex;justify-content:space-between;font-size:4.5px;color:var(--muted)}
.ph{position:absolute}
/* slide 1 */
.s1 .ph{left:22px;top:24px;width:230px;height:150px;background:linear-gradient(135deg,#e9eef6,#cfdcee 45%,#f3e6d8)}
.s1 .tagline{position:absolute;right:18px;top:184px;font-size:12px;font-weight:700}
/* slide 2 */
.row{position:absolute;left:18px;right:14px;height:40px;display:flex;gap:4px}
.row .ph{position:relative;width:66px;height:40px;background:linear-gradient(135deg,#0e2346,#3a6fb0)}
.row .ph span{position:absolute;left:4px;bottom:3px;font-size:5px;color:#fff;font-weight:700}
.row .box{flex:1;background:var(--blue);color:#fff;font-size:5.2px;line-height:1.35;padding:4px 6px}
.row .list{display:grid;grid-template-columns:1fr 1fr;gap:3px 8px;padding:5px 8px}
.r1{top:70px}.r2{top:116px}.r3{top:162px}
/* slide 3 */
.s3 .ph{left:18px;top:70px;width:130px;height:108px;background:linear-gradient(160deg,#f4f4f2,#dfe3ea)}
.alert{position:absolute;font-size:6px;font-weight:700;color:var(--alert)}
.chart-title{position:absolute;left:170px;top:70px;width:140px;text-align:center;font-size:5.8px;line-height:1.3}
.quote{position:absolute;left:0;right:0;top:198px;text-align:center;font-size:6.2px;font-style:italic}
/* slide 5 */
.refs{position:absolute;left:18px;top:66px;width:300px;display:grid;grid-template-columns:repeat(3,1fr);gap:4px}
.ref{height:42px;border:1px solid var(--frame);padding:3px 4px;font-size:4.4px;line-height:1.3}
.ref b{display:block;font-size:7px;color:var(--ink);margin-bottom:2px}
/* slide 6 */
.group{position:absolute;left:18px;right:14px;border:1px solid var(--frame);padding:3px 6px}
.group h3{font-size:5.5px;margin-bottom:3px}
.badges{display:grid;gap:6px 10px}
.badge{height:13px;background:#d9e1ec;border-radius:2px}
.badge.alt{background:#e9d7e4}
/* slide 7 */
.s7 .ph{left:18px;top:110px;width:130px;height:80px;background:linear-gradient(135deg,#9aa0a6,#d6d3cc)}
.connect{position:absolute;left:162px;top:120px;width:150px;text-align:center}
.connect h2{font-size:10.5px;margin-bottom:10px}
.connect p{font-size:6px;line-height:1.35}
.social{display:flex;gap:3px;justify-content:center;margin-top:4px}
.social span{width:9px;height:9px;background:var(--blue-dark);border-radius:1px}
</style>
</head>
<body>

<section class="slide s1">
  <div class="brand">n-stride</div>
  <div class="ph" role="img" aria-label="Word cloud of software terms around the word CODING"></div>
  <p class="tagline">Software Quality Experts</p>
  <div class="footer"><span>11/25/2019</span><span>www.n-stride.example</span><span>1</span></div>
</section>

<section class="slide s2">
  <div class="brand">n-stride</div>
  <h1 class="slide-title">We are fully dedicated to software quality services.</h1>
  <div class="row r1">
    <div class="ph" role="img" aria-label="Close-up of an eye with digital overlay"><span>Our vision</span></div>
    <p class="box">Our vision recognizes that developers and organizations need to integrate efficient quality assurance into the software lifecycle, while freeing up resources, cutting costs, and supporting regulatory compliance.</p>
  </div>
  <div class="row r2">
    <div class="ph" role="img" aria-label="Blue digital network landscape"><span>Our mission</span></div>
    <p class="box">We help organizations develop application testing strategies and execution models that focus on defect prevention. We build a service company by developing talent, which enable us to help our customers concentrate on their application delivery goals.</p>
  </div>
  <div class="row r3">
    <div class="ph" role="img" aria-label="Business professional in a suit"><span>Our vision</span></div>
    <div class="box list"><span>➤ Passion for Quality</span><span>➤ Responsibility</span><span>➤ Problem solvers</span><span>➤ Honesty</span><span>➤ Adding value oriented</span><span>➤ Integrity</span></div>
  </div>
  <div class="footer"><span>11/25/2019</span><span>www.n-stride.example</span><span>2</span></div>
</section>

<section class="slide s3">
  <div class="brand">n-stride</div>
  <h1 class="slide-title">Market studies demonstrate the need of tracking defects earlier.</h1>
  <div class="ph" role="img" aria-label="Man drawing software sketches on a whiteboard"></div>
  <span class="alert" style="left:22px;top:72px">Software quality matters if you ...</span>
  <span class="alert" style="left:30px;top:181px">Need to detect faults earlier !</span>
  <p class="chart-title">Relative Cost to Repair a Defect at Different Project Lifecycle Phases</p>
  <svg style="position:absolute;left:180px;top:90px" width="120" height="100" viewBox="0 0 120 100" font-family="Arimo, sans-serif" font-size="5" text-anchor="middle">
    <polygon points="60,4 68,20 52,20" fill="#9dc3e6"/>
    <polygon points="52,20 68,20 75,34 45,34" fill="#bdd7ee"/>
    <polygon points="45,34 75,34 82,48 38,48" fill="#dbe9f6"/>
    <polygon points="38,48 82,48 89,62 31,62" fill="#9dc3e6"/>
    <polygon points="31,62 89,62 96,76 24,76" fill="#5b9bd5"/>
    <text x="60" y="30">10</text><text x="60" y="44">20</text><text x="60" y="58">50</text><text x="60" y="72" fill="#fff">100</text>
    <g font-size="3.8" text-anchor="start" fill="#444">
      <rect x="20" y="82" width="3" height="3" fill="#5b9bd5"/><text x="25" y="85">Production</text>
      <rect x="48" y="82" width="3" height="3" fill="#9dc3e6"/><text x="53" y="85">Acceptance Test</text>
      <rect x="82" y="82" width="3" height="3" fill="#dbe9f6"/><text x="87" y="85">Test</text>
      <rect x="20" y="90" width="3" height="3" fill="#bdd7ee"/><text x="25" y="93">Coding</text>
      <rect x="48" y="90" width="3" height="3" fill="#9dc3e6"/><text x="53" y="93">Design</text>
      <rect x="82" y="90" width="3" height="3" fill="#5b9bd5"/><text x="87" y="93">Requirements</text>
    </g>
  </svg>
  <p class="quote">“On average, more than 50 percent of IT projects are at risk”</p>
  <div class="footer"><span>11/25/2019</span><span>www.n-stride.example</span><span>3</span></div>
</section>

<section class="slide s4">
  <div class="brand">n-stride</div>
  <h1 class="slide-title">n-stride provides a wide range of quality services.</h1>
  <svg style="position:absolute;left:0;top:70px" width="334" height="160" viewBox="0 0 334 160" font-family="Arimo, sans-serif" text-anchor="middle">
    <text transform="translate(14,80) rotate(-90)" font-size="6.5" font-weight="700" fill="#1d2438">Software Development Life Cycle</text>
    <text x="180" y="8" font-size="8" font-weight="700" fill="#b5008c">n-stride Services</text>
    <g fill="#9dc3e6">
      <polygon points="28,16 102,16 114,36 102,56 28,56 38,36"/>
      <polygon points="114,16 194,16 206,36 194,56 114,56 124,36"/>
      <polygon points="206,16 288,16 300,36 288,56 206,56 216,36"/>
    </g>
    <g fill="#2f5597"><circle cx="54" cy="36" r="14"/><circle cx="142" cy="36" r="14"/><circle cx="234" cy="36" r="14"/></g>
    <g fill="#fff" font-size="4.5"><text x="54" y="38">PLAN</text><text x="142" y="38">BUILD</text><text x="234" y="35">DELIVER</text><text x="234" y="41">&amp; MAINTAIN</text></g>
    <g fill="#1d2438" font-size="5"><text x="85" y="34">6 months</text><text x="85" y="41">- 1 year</text><text x="173" y="34">1 - 3</text><text x="173" y="41">year</text><text x="266" y="34">Typically</text><text x="266" y="41">10 years</text></g>
    <text x="180" y="76" font-size="8" font-weight="700" fill="#b5008c">Methodology, Tools and Training</text>
    <g fill="#2f5597"><rect x="34" y="90" width="70" height="30"/><rect x="130" y="90" width="70" height="30"/><rect x="226" y="90" width="70" height="30"/></g>
    <g fill="#9dc3e6"><polygon points="108,99 120,99 120,95 127,105 120,115 120,111 108,111"/><polygon points="204,99 216,99 216,95 223,105 216,115 216,111 204,111"/></g>
    <g fill="#fff" font-size="5" font-weight="700"><text x="69" y="107">QA Consulting</text><text x="165" y="103">Consulting &amp;</text><text x="165" y="110">Implementation</text><text x="165" y="117">Services</text><text x="261" y="103">Test Automation</text><text x="261" y="110">Non-Regression</text><text x="261" y="117">Testing</text></g>
  </svg>
  <div class="footer"><span>11/25/2019</span><span>www.n-stride.example</span><span>4</span></div>
</section>

<section class="slide s5">
  <div class="brand">n-stride</div>
  <h1 class="slide-title">Project references.</h1>
  <div class="refs">
    <div class="ref"><b>Banque Meridia</b>• Test Process Assessment<br>• Testing &amp; Acceptance Framework</div>
    <div class="ref"><b>Ministère du Commerce</b>• Data Mining<br>• Business Intelligence<br>• Geo Information System</div>
    <div class="ref"><b>NordLink</b>• Cloud Quality Assurance</div>
    <div class="ref"><b>Helix Labs</b>• Requirement, Risk and Solution Analysis</div>
    <div class="ref"><b>BioVault</b>• User Acceptance Testing</div>
    <div class="ref"><b>Novaterra</b>• Business Process Engineering<br>• API Test Automation</div>
    <div class="ref"><b>Grove Partners</b>• Test Process Assessment</div>
    <div class="ref"><b>eCare</b>• Information Security Policy<br>• Quality Review</div>
    <div class="ref"><b>DMC</b>• Data Mining and BI<br>• G.I.S.</div>
  </div>
  <div class="footer"><span>11/25/2019</span><span>www.n-stride.example</span><span>5</span></div>
</section>

<section class="slide s6">
  <div class="brand">n-stride</div>
  <h1 class="slide-title">Partners, memberships and certifications.</h1>
  <div class="group" style="top:62px;height:100px">
    <h3>Partners</h3>
    <div class="badges" style="grid-template-columns:repeat(4,1fr);gap:12px 14px;padding:4px 6px">
      <span class="badge"></span><span class="badge"></span><span class="badge alt"></span><span class="badge"></span>
      <span class="badge"></span><span class="badge alt"></span><span class="badge"></span><span class="badge"></span>
      <span class="badge alt"></span><span class="badge"></span><span class="badge"></span><span class="badge alt"></span>
    </div>
  </div>
  <div class="group" style="top:168px;height:52px">
    <h3>Memberships &amp; Certifications</h3>
    <div class="badges" style="grid-template-columns:repeat(6,1fr);padding:4px 2px">
      <span class="badge"></span><span class="badge alt"></span><span class="badge"></span><span class="badge alt"></span><span class="badge"></span><span class="badge"></span>
    </div>
  </div>
  <div class="footer"><span>11/25/2019</span><span>www.n-stride.example</span><span>6</span></div>
</section>

<section class="slide s7">
  <div class="brand">n-stride</div>
  <h1 class="slide-title" style="top:46px">Any questions ?</h1>
  <div class="ph" role="img" aria-label="Two children sitting on the floor talking through a string phone"></div>
  <div class="connect">
    <h2>Let’s Connect !</h2>
    <p>www.n-stride.example<br>contact@n-stride.example<br>Phone: +352 20 000 000</p>
    <div class="social" aria-label="Social media links"><span></span><span></span><span></span><span></span></div>
  </div>
  <div class="footer"><span>11/25/2019</span><span>www.n-stride.example</span><span>7</span></div>
</section>

</body>
</html>
```